A5 flyer required for motorcycle tracking device - Easy.

We are a UK company who supply pizza delivery bikes, we now also supply "Motorcycle tracking devices"..
We want the flyer to be in similiar style to that of our new to be website design so that there is consistancy throughout.

Reason: Extended due to information not being present - my mistake apologies!

Hi Designers!

Please use the "Fellani pizza" delivery bike as supplied in the brief (Blue bike with box on), if you require a different image etc just let me know & I`ll upload. Also somewhere on the flyer this information needs to be added..

"Kit consists: Motorcycle Tracker
                    Internal battery
                    Connection leads
                    Full Instructions"

Just so they understand what it is that they are purchasing......Thank You!

Target Market(s)

Owners and managers more importantly these people loose revenue from stolen bikes,mostly males between age of 30 to 50

Industry/Entity Type

Pizza Delivery

Requirements
Must have
• One single side in colour must incorporate an image of the QR240-7K motorcycle that we sell but only as a small feature which could be part of an easy step guide, the emphassis needs to be on the tracker itself.
• All the bullet points listed in the word doc uploaded. Maybe one hard hitting line to head like "Purchasing this could seriously protect your wealth"...sort of thing, you get the idea.
• Reference to www.trundlecart.co.uk as shown and in the same design/font on our website but as the new homepage design
Nice to have
• Would be nice if the customer could see in easy steps how the tracker would intergrate with their current motorcycle ie, Purchase tracker from us, Insert PAYG sim card, Install tracker into motorcycle (Just 2 wires required)...then track their asset(Motorcycle) with their mobile phone (Preferable) or internet

```html
<!DOCTYPE html>
<html lang="en">
<head>
<meta charset="utf-8">
<title>Track your motorcycle – Trundlecart</title>
<link href="https://fonts.googleapis.com/css2?family=Open+Sans:ital,wght@0,600;0,700;0,800;1,700;1,800&display=swap" rel="stylesheet">
<style>
  :root {
    --bg: #1d1d1d;
    --white: #ffffff;
    --off-white: #ececec;
    --gold: #f2a91b;
    --gold-deep: #d98a0c;
    --grey: #b9b9b9;
  }
  html, body { margin: 0; padding: 0; overflow: hidden; }
  body { background: var(--bg); }
  .flyer {
    position: relative;
    width: 846px;
    height: 1200px;
    overflow: hidden;
    background: var(--bg);
    font-family: "Open Sans", Arial, sans-serif;
    color: var(--white);
  }
  .flyer > * { position: absolute; margin: 0; }
  .gold { color: var(--gold); }

  .site-url { left: 21px; top: 16px; font-size: 25px; font-weight: 800; color: var(--off-white); letter-spacing: 0.2px; }
  .offer { right: 22px; top: 12px; text-align: right; }
  .offer-title { margin: 0; font-size: 23px; font-weight: 800; color: var(--gold); }
  .offer-price { margin: 4px 8px 0 0; font-size: 14.5px; font-weight: 700; line-height: 1.3; text-align: center; }

  .headline { left: 0; width: 846px; top: 78px; text-align: center; font-weight: 800; line-height: 1.02; }
  .headline-main { display: block; font-size: 60px; letter-spacing: -1px; }
  .headline-main .gold { background: linear-gradient(180deg, #ffc63a, var(--gold-deep)); -webkit-background-clip: text; background-clip: text; color: transparent; }
  .headline-sub { display: block; margin-top: 10px; font-size: 25px; color: var(--gold); }

  .step-num { font-size: 64px; font-weight: 800; font-style: italic; color: var(--gold); line-height: 1; }
  .step-title { font-size: 27px; font-weight: 800; line-height: 1; }
  .step-note { text-align: center; font-weight: 700; line-height: 1.45; }

  .placeholder { border-radius: 6px; }
  .sim-card { left: 560px; top: 288px; width: 104px; height: 54px; background: linear-gradient(135deg, #d9d9d9, #a9a9a9); transform: rotate(6deg); }
  .tracker { left: 167px; top: 391px; width: 214px; height: 106px; background: linear-gradient(180deg, #4a4a50, #1f1f24); border-radius: 14px 14px 24px 24px; }
  .tracker-caption { left: 150px; top: 520px; width: 270px; font-size: 12px; color: var(--gold); line-height: 1.4; }

  .battery-note { left: 540px; top: 505px; width: 290px; font-size: 15.5px; font-style: italic; line-height: 1.4; }

  .tagline { left: 0; width: 846px; top: 719px; text-align: center; font-size: 27px; font-weight: 800; font-style: italic; color: var(--off-white); }

  .bike { left: 37px; top: 793px; width: 312px; height: 180px; background: linear-gradient(180deg, #2f7fd6 0%, #1b3fa8 55%, #2a2a30 100%); }
  .model-label { left: 317px; top: 836px; font-size: 17px; font-weight: 800; }
  .bike-caption { left: 20px; top: 978px; width: 340px; font-size: 16.5px; font-style: italic; line-height: 1.35; }

  .kit { left: 508px; top: 820px; }
  .kit-title { margin: 0 0 4px; font-size: 32px; font-weight: 800; font-style: italic; color: var(--gold); }
  .kit-list { list-style: none; margin: 0; padding: 0; font-size: 23px; font-weight: 700; line-height: 1.3; }

  .enquiries { left: 0; width: 846px; top: 1038px; text-align: center; font-size: 35px; font-weight: 800; color: var(--off-white); line-height: 1.2; }
  .phone { display: block; font-size: 38px; color: var(--gold); letter-spacing: 1px; }
  .running-cost { left: 0; width: 846px; top: 1131px; text-align: center; font-size: 24px; font-weight: 800; font-style: italic; }
  .footnote { left: 0; width: 846px; top: 1167px; text-align: center; font-size: 11px; font-weight: 700; font-style: italic; color: var(--gold); }
</style>
</head>
<body>
<main class="flyer">
  <p class="site-url">WWW.<span class="gold">TRUNDLECART</span>.CO.UK</p>

  <div class="offer">
    <p class="offer-title">No yearly subscription!</p>
    <p class="offer-price">One off fee of £125 per tracker +<br>£10 per PAYG SIM card</p>
  </div>

  <h1 class="headline">
    <span class="headline-main"><span class="gold">Track</span> your<br>motorcycle!</span>
    <span class="headline-sub">in 3 easy steps</span>
  </h1>

  <span class="step-num" style="left:108px;top:276px;">1</span>
  <p class="step-title" style="left:148px;top:300px;">insert the PAYG sim card</p>
  <div class="placeholder sim-card" role="img" aria-label="Photo of a PAYG SIM card"></div>

  <div class="placeholder tracker" role="img" aria-label="Photo of the black motorcycle tracker unit"></div>
  <p class="step-note tracker-caption">Small size 9cm H 5cm W 2cm D,<br>can easily be hidden.</p>

  <span class="step-num" style="left:504px;top:400px;">2</span>
  <p class="step-title" style="left:558px;top:416px;">install our device</p>
  <p class="step-note gold" style="left:560px;top:448px;width:284px;font-size:15.5px;">with just 2 wires!</p>
  <p class="step-note battery-note">Battery will function up<br>to <span class="gold">14 days</span> even after ignition<br>is turned off!</p>

  <span class="step-num" style="left:111px;top:592px;">3</span>
  <p class="step-title" style="left:169px;top:606px;">start tracking!</p>
  <p class="step-note" style="left:140px;top:640px;width:240px;font-size:15.5px;line-height:1.35;">on your <span class="gold">mobile phone</span> via<br>skyglobe maps for <span class="gold">free</span>!</p>

  <p class="tagline">Can you seriously afford <span class="gold">not</span> to be without one of these?</p>

  <div class="placeholder bike" role="img" aria-label="Photo of the blue QR240-7K delivery motorcycle with a Fellani pizza box on the back"></div>
  <p class="model-label">QR240-7K</p>
  <p class="step-note bike-caption">Easily transferable between bikes<br>via <span class="gold">quick connectors</span>!</p>

  <section class="kit">
    <h2 class="kit-title">Kit Consists of:</h2>
    <ul class="kit-list">
      <li>- motorcycle tracker</li>
      <li>- connection leads</li>
      <li>- full instructions</li>
    </ul>
  </section>

  <p class="enquiries">Enquires will be answered immediately on<span class="phone">07700 900417.</span></p>
  <p class="running-cost">As little as <span class="gold">40p per year</span> to use/ maintain!*</p>
  <p class="footnote">*(SIM card requires 1 use, 1 txt per 3 months to remain active)</p>
</main>
</body>
</html>
```